Open Doors Sermon Series

Design a 4x6 Double Sides Digital Postcard for our new sermon series...begins Sunday.

Here is info on the Sermon Series:

Sermon Series Title: Open Doors

Sermon Series Description: The goal of the “Open Doors” series is to turn followers into fishermen. If you’ve ever gone fishing, then you know that one of the most exciting feelings in the world is that underwater tug on the other end of the line. That is the feeling true fishermen get hooked on and want to experience again and again.
Our Lord Jesus and his fishermen disciples knew all about that. In Matthew 4:19, Jesus gave a different kind of fishing invitation to two brothers who were casting nets into the sea. He said, “Follow me, and I will make you fishers of men.”
Modern day disciples are still being found by Jesus and accepting his invitation to find people for Jesus. Are you one of them? As we prepare to move to our new church home, it takes found people to find people and invite them to church. So come and learn how to cast your own net and what to do when you feel the tug of the BIG ONE.

Assignments:
June 1, 2014 - Walk With Open Hands
June 8, 2014 - Hunger for a Harvest
June 15, 2014 - Father's Day
June 22, 2014 - The Far End of the Valley

Worship Times:
9:55 AM - Traditional Worship
12:00 PM - Contemporary Worship

Church name: Maplecrest Road Congregational Church

Leadership:
Rev. Delphine Harlow Okafor, Senior Pastor & Teacher

Contact Information:
4100 Maplecrest Rd.
Cleveland, OH 44115
216.555.0148
www.mrcc-ps.example

```html
<!DOCTYPE html>
<html lang="en">
<head>
<meta charset="utf-8">
<title>Open Doors Sermon Series Postcard</title>
<link href="https://fonts.googleapis.com/css2?family=Open+Sans:wght@400;600&family=UnifrakturMaguntia&display=swap" rel="stylesheet">
<style>
  :root {
    --page: #ecebe8;
    --sea-deep: #0d3a8a;
    --sea-mid: #1d5fc0;
    --sea-light: #6fb8ea;
    --wood: #6b4a2c;
    --white: #ffffff;
    --ink-soft: #e8f1ff;
    --photo: #5a6470;
  }
  * { box-sizing: border-box; margin: 0; padding: 0; }
  html, body { width: 1200px; height: 1000px; overflow: hidden; background: var(--page); }
  .canvas { position: relative; width: 1200px; height: 1000px; }

  .postcard { position: absolute; width: 660px; height: 440px; overflow: hidden;
    box-shadow: 0 4px 14px rgba(0,0,0,.25); }

  /* Front */
  .postcard--front { left: 30px; top: 40px;
    background: linear-gradient(180deg, var(--sea-mid) 0%, var(--sea-deep) 55%, var(--sea-mid) 100%); }
  .front-scene { position: absolute; left: 0; top: 0; width: 100%; height: 175px;
    background: linear-gradient(180deg, var(--sea-light) 0%, var(--sea-mid) 70%, rgba(29,95,192,0) 100%),
                linear-gradient(90deg, var(--wood) 0%, transparent 30%); }
  .front-scene::before { content: ""; position: absolute; left: 0; top: 0; width: 200px; height: 180px;
    background: radial-gradient(ellipse at top left, rgba(107,74,44,.7), transparent 70%); }
  .start-date { position: absolute; right: 40px; top: 26px; font-family: "UnifrakturMaguntia", serif;
    font-size: 26px; color: var(--white); }
  .front-copy { position: absolute; left: 26px; top: 180px; right: 26px; color: var(--white);
    font-family: "Open Sans", sans-serif; font-size: 13.4px; line-height: 1.32; text-align: justify; }
  .series-title { float: left; font-family: "UnifrakturMaguntia", serif; font-weight: 400;
    font-size: 84px; line-height: 84px; margin: -6px 14px 0 0;
    background: linear-gradient(180deg, var(--white) 30%, var(--sea-light) 100%);
    -webkit-background-clip: text; background-clip: text; color: transparent; }
  .front-copy p + p { margin-top: 14px; }

  /* Back */
  .postcard--back { left: 510px; top: 510px;
    background: linear-gradient(90deg, var(--sea-deep) 0%, var(--sea-mid) 46%, #a9c7ee 56%, var(--white) 68%); }
  .back-scene { position: absolute; left: 0; top: 0; width: 100%; height: 120px;
    background: linear-gradient(180deg, var(--wood) 0%, var(--sea-light) 40%, rgba(111,184,234,0) 100%);
    -webkit-mask-image: linear-gradient(90deg, #000 60%, transparent 90%);
    mask-image: linear-gradient(90deg, #000 60%, transparent 90%); }
  .back-info { position: absolute; left: 22px; top: 78px; width: 340px; color: var(--white);
    font-family: "Open Sans", sans-serif; font-size: 14px; line-height: 1.3; }
  .section-heading { font-family: "UnifrakturMaguntia", serif; font-weight: 400; font-size: 25px;
    line-height: 1; margin-bottom: 2px; }
  .schedule { list-style: none; }
  .row { display: flex; gap: 10px; margin-top: 12px; }
  .pastor-photo { width: 96px; height: 112px; background: linear-gradient(180deg, #7a838d, var(--photo));
    flex: none; }
  .leadership { margin-top: 8px; }
  .church-name { position: absolute; left: 22px; top: 362px; display: flex; align-items: center; gap: 10px;
    font-family: "Open Sans", sans-serif; font-size: 18px; color: var(--white); font-weight: 400; }
  .church-name .mark { width: 16px; height: 16px; background: var(--white); flex: none; }
  .contact { position: absolute; left: 22px; top: 394px; font-family: "Open Sans", sans-serif;
    font-size: 12.5px; line-height: 1.35; color: var(--ink-soft); }
</style>
</head>
<body>
<main class="canvas">

  <section class="postcard postcard--front">
    <div class="front-scene" role="img" aria-label="Photo of a wooden boat hull and a rope fishing net over blue water"></div>
    <p class="start-date">Starts June 1st</p>
    <div class="front-copy">
      <h1 class="series-title">Open Doors</h1>
      <p>The goal of the “Open Doors” series is to turn followers into fishermen. If you’ve ever gone fishing, then you know that one of the most exciting feelings in the world is that underwater tug on the other end of the line. That is the feeling true fishermen get hooked on and want to experience again and again. Our Lord Jesus and his fishermen disciples knew all about that. In Matthew 4:19, Jesus gave a different kind of fishing invitation to two brothers who were casting nets into the sea. He said, “Follow me, and I will make you fishers of men.”</p>
      <p>Modern day disciples are still being found by Jesus and accepting his invitation to find people for Jesus. Are you one of them? As we prepare to move to our new church home, it takes found people to find people and invite them to church. So come and learn how to cast your own net and what to do when you feel the tug of the BIG ONE.</p>
    </div>
  </section>

  <section class="postcard postcard--back">
    <div class="back-scene" role="img" aria-label="Photo of a wooden boat edge and fishing net above blue water"></div>
    <div class="back-info">
      <h2 class="section-heading">Assignments:</h2>
      <ul class="schedule">
        <li>June 1, 2014 - Walk With Open Hands</li>
        <li>June 8, 2014 - Hunger for a Harvest</li>
        <li>June 15, 2014 - Father's Day</li>
        <li>June 22, 2014 - The Far End of the Valley</li>
      </ul>
      <div class="row">
        <div class="pastor-photo" role="img" aria-label="Portrait photo of the senior pastor"></div>
        <div>
          <h2 class="section-heading">Worship Times:</h2>
          <p>9:55 AM - Traditional Worship<br>12:00 PM - Contemporary Worship</p>
          <div class="leadership">
            <h2 class="section-heading">Leadership:</h2>
            <p>Rev. Delphine Harlow Okafor<br>Senior Pastor &amp; Teacher</p>
          </div>
        </div>
      </div>
    </div>
    <p class="church-name"><span class="mark"></span>Maplecrest Road Congregational Church</p>
    <p class="contact">4100 Maplecrest Rd. &nbsp;|&nbsp; Cleveland, OH 44115<br>PH: 216.555.0148 &nbsp;|&nbsp; www.mrcc-ps.example</p>
  </section>

</main>
</body>
</html>
```